Rising Side by Side A Handbook to Help Managers and Crews Climb to Fresh Peaks of Results

We need a book cover design for a book titled: Rising Side by Side:
A Handbook to Help Managers and Crews Climb to Fresh Peaks of Results
The book is intended to enhance the author's personal brand and promote the author's consulting services. The book also teaches: How To Help Leaders and Teams Reach New Heights of Performance. I would like to use the colors from the www.bramblewickadvisory.example website (blue and orange). The design should communicate credibility and expertise in the topic of the book.

Target Market(s)

Municipal and Industrial and Energy Industry Team Leaders and Teams

Industry/Entity Type

water and waste water, energy, power generation, petrochmical

Requirements
Must have
• Look like a Kestrel Ledger best seller. Look professional and appealling
Nice to have
• Sell at the airport. Executives keep in their office.
Should not have
• Do not plagiarize.

```html
<!DOCTYPE html>
<html lang="en">
<head>
<meta charset="utf-8">
<title>Rising Side by Side – Book Cover Spread</title>
<link rel="stylesheet" href="https://fonts.googleapis.com/css2?family=Oswald:wght@500&family=Raleway:wght@400;500&family=Source+Sans+3:wght@400&display=swap">
<style>
  :root {
    --orange: #f7972a;
    --navy: #0f2a5c;
    --ink: #1a1a1a;
    --paper: #ffffff;
    --skin-dark: #6b4330;
    --skin-mid: #a6715a;
  }
  html, body {
    margin: 0;
    padding: 0;
    width: 1200px;
    height: 1200px;
    overflow: hidden;
    background: var(--paper);
  }
  .canvas {
    position: relative;
    width: 1200px;
    height: 1200px;
    background: var(--paper);
  }
  .spread {
    position: absolute;
    left: 0;
    top: 160px;
    width: 1200px;
    height: 882px;
    background: var(--paper);
    box-shadow: 0 2px 10px rgba(0,0,0,0.35);
  }
  /* Back cover */
  .back-cover {
    position: absolute;
    left: 0; top: 0;
    width: 588px; height: 882px;
  }
  .back-copy {
    position: absolute;
    left: 69px;
    width: 453px;
    font-family: "Source Sans 3", sans-serif;
    font-size: 16px;
    line-height: 21.8px;
    color: var(--ink);
    text-align: justify;
    margin: 0;
  }
  .back-copy.first { top: 79px; }
  .back-copy.second { top: 384px; }
  .divider {
    position: absolute;
    top: 524px;
    left: 0;
    width: 588px;
    text-align: center;
    font-family: "Source Sans 3", sans-serif;
    font-size: 14px;
    letter-spacing: 26px;
    padding-left: 18px;
    box-sizing: border-box;
    color: var(--ink);
  }
  .author-photo {
    position: absolute;
    left: 68px; top: 559px;
    width: 137px; height: 189px;
    background: linear-gradient(160deg, #5a5350 0%, #3a3432 60%, #262120 100%);
  }
  .author-bio {
    position: absolute;
    left: 220px; top: 557px;
    width: 302px;
    margin: 0;
    font-family: "Source Sans 3", sans-serif;
    font-size: 13px;
    line-height: 16.4px;
    text-align: justify;
    color: var(--ink);
  }
  /* Spine */
  .spine {
    position: absolute;
    left: 588px; top: 0;
    width: 26px; height: 882px;
    background: var(--orange);
  }
  /* Front cover */
  .front-cover {
    position: absolute;
    left: 614px; top: 0;
    width: 586px; height: 882px;
    overflow: hidden;
  }
  .hands-art {
    position: absolute;
    left: 0; top: 280px;
    width: 586px; height: 602px;
    background:
      radial-gradient(ellipse 190px 330px at 272px 330px, var(--paper) 70%, rgba(255,255,255,0) 100%),
      linear-gradient(90deg, var(--skin-dark) 0%, var(--skin-mid) 30%, #ffffff 50%, var(--skin-mid) 70%, var(--skin-dark) 100%);
  }
  .title {
    position: absolute;
    left: 0; width: 586px;
    margin: 0;
    text-align: center;
    font-family: "Oswald", sans-serif;
    font-weight: 500;
    text-transform: uppercase;
    line-height: 1;
  }
  .title-top {
    top: 42px;
    font-size: 148px;
    color: var(--orange);
    letter-spacing: 4px;
  }
  .title-bottom {
    top: 188px;
    font-size: 82px;
    color: var(--navy);
    letter-spacing: 5px;
  }
  .subtitle {
    position: absolute;
    left: 82px; top: 396px;
    width: 380px;
    margin: 0;
    text-align: center;
    font-family: "Raleway", sans-serif;
    font-weight: 500;
    font-size: 23px;
    line-height: 37.5px;
    color: var(--navy);
  }
  .author-name {
    position: absolute;
    left: 60px; top: 768px;
    width: 392px;
    margin: 0;
    text-align: center;
    font-family: "Raleway", sans-serif;
    font-weight: 400;
    font-size: 34px;
    line-height: 47px;
    letter-spacing: 8px;
    color: var(--navy);
  }
</style>
</head>
<body>
<div class="canvas">
  <div class="spread">
    <section class="back-cover">
      <p class="back-copy first">Lorem ipsum dolor sit amet, consectetur adipiscing elit. Nunc volutpat fermentum nisl, faucibus pretium arcu fringilla vitae. Aenean vel dui tortor. Curabitur dictum felis ac molestie sagittis. Maecenas lobortis ornare nisi. Duis in auctor nisl. Etiam lectus eros, congue id congue sed, eleifend nec ex. Donec id diam luctus, efficitur ipsum sit amet, euismod mi. Etiam hendrerit urna ex, sit amet varius est tempor et. Phasellus egestas neque dui, sit amet faucibus enim semper vitae. Mauris eu orci tempus, vulputate nunc sit amet, pretium tortor. Sed sodales dolor quis nisi fringilla, non hendrerit arcu aliquet. Ut sed elementum diam, aliquam porta odio. Nam efficitur arcu ipsum, in egestas sapien lacinia nec. Nam ut tortor purus. Cras blandit ante nec semper pellentesque. Nunc tristique faucibus augue id rhoncus.</p>
      <p class="back-copy second">Orci varius natoque penatibus et magnis dis parturient montes, nascetur ridiculus mus. Curabitur non congue eros, at tempus dolor. Sed nunc dolor, varius eget elit aliquam, tincidunt varius sapien. Integer aliquet nisi ante, quis venenatis ex ornare quis. Fusce at leo ligula. Aenean laoreet erat ac mauris lacinia maximus. Duis eget tincidunt lectus.</p>
      <div class="divider">***</div>
      <div class="author-photo" role="img" aria-label="Portrait photo of the author in a dark suit"></div>
      <p class="author-bio">Maecenas non pellentesque lectus, non feugiat leo. Aliquam lectus nulla, sollicitudin nec tristique condimentum, lacinia vel enim. Donec gravida mauris vel ligula eleifend finibus. Fusce luctus sit amet tellus eget iaculis. Aenean commodo purus purus, ac lobortis tortor porta ac. Proin sed nisi eget neque commodo interdum. Praesent sit amet vestibulum mauris. Cras id ullamcorper est, aliquet posuere tellus. Donec fermentum sem diam. Suspendisse ornare, lorem et dignissim facilisis, dui metus euismod dui, ac euismod nulla tellus eu magna.</p>
    </section>

    <div class="spine"></div>

    <section class="front-cover">
      <div class="hands-art" role="img" aria-label="Photo of many diverse hands joined together forming the outline of a light bulb, with a metal bulb base at the bottom"></div>
      <h1 class="title title-top">Rising</h1>
      <h1 class="title title-bottom">Side by Side</h1>
      <p class="subtitle">A Handbook<br>to Help Managers<br>and Crews Climb<br>to Fresh Peaks of<br>Results</p>
      <p class="author-name">AUTHOR<br>NAME</p>
    </section>
  </div>
</div>
</body>
</html>
```